Health and Wellness. I am an energetic, but not over the top, Certified Personal Trainer and Nutriti

I need a flyer, 8.5 x 11, representing my company to be displayed in a Doctor's office that specializes in Pain Medicine. Most, if not all, of these clients experience pain or have some chronic diseases such as high blood pressure, high cholesterol, back pain, joint pain, etc. So the flyer should convey that exercise and nutrition reduce/relieves pain and references some of these ailments. Ideally, the flyer should depict an overweight person exercising with a content, or somewhat content or smiling expression on their face in some part of the flyer. My services cover nutrition and include personal training to where I Ideally train people in their home, equipment permitting, or outside in our local Floridian Parks, and sometimes beaches. This flyer will be in a display case, and the bottom right 8.5 x5 cm will need to be blank, or allow for me to input the back of my business car into it, as I'll have business cards readily available in front of the flyer to be taken. I've included some versions of my logos to be added to the flyer. The other picture is of the flyer holder, with business card area, that this flyer will be presented in. Finally, I've attached a pic of what the back of my business card looks like to be input into that bottom right hand corner. You'll be able to see the area in the bottom right that will display my business cards.
Target Market(s)
People looking for weight loss through Nutrition and Fitness. Those looking to relieve joint and/or back pain or those with Chronic diseases such as high blood pressure, high cholesterol, etc.
Industry/Entity Type
Doctor
Requirements
Must have
- Resemble my Logo's color scheme: Red, Teal, and Grey. Some type of photo of an overweight or slightly overweight person exercising.

```html
<!DOCTYPE html>
<html lang="en">
<head>
<meta charset="utf-8">
<title>Kessler's Fitness Flyer</title>
<link rel="stylesheet" href="https://fonts.googleapis.com/css2?family=Fira+Sans+Extra+Condensed:wght@400;500&family=Open+Sans:ital,wght@0,400;1,700&display=swap">
<style>
  :root {
    --backdrop: #636363;
    --brand-red: #ec1c24;
    --head-red: #e8424a;
    --panel-grey: #7d7e81;
    --name-grey: #b4b6ba;
    --paper: #ffffff;
    --card-text: #e6e6e6;
  }
  * { margin: 0; padding: 0; box-sizing: border-box; }
  html, body { width: 1014px; height: 1200px; overflow: hidden; background: var(--backdrop); }
  .flyer {
    position: absolute; left: 149px; top: 114px;
    width: 850px; height: 1100px;
    transform: scale(0.8675); transform-origin: 0 0;
    box-shadow: 0 6px 14px rgba(0,0,0,.45);
    overflow: hidden;
    font-family: "Fira Sans Extra Condensed", "Arial Narrow", sans-serif;
  }
  .flyer-shapes { position: absolute; inset: 0; }
  .brand-name {
    position: absolute; left: 18px; top: 86px; width: 260px;
    text-align: center;
    font-weight: 500; font-size: 30px; line-height: 36px;
    color: var(--name-grey);
    white-space: nowrap;
  }
  .trainer-photo {
    position: absolute; left: 567px; top: 323px;
    width: 244px; height: 244px; border-radius: 50%;
    border: 4px solid var(--paper);
    background: radial-gradient(circle at 45% 45%, #6b7d5e 0%, #4f5f46 45%, #8a9480 100%);
  }
  .headline {
    position: absolute; left: 0; top: 600px; width: 516px;
    text-align: center; color: var(--head-red);
    font-weight: 400; font-size: 52px; line-height: 72px;
    letter-spacing: -1.3px;
  }
  .pitch {
    position: absolute; left: 520px; width: 336px;
    text-align: center; color: var(--paper);
    font-weight: 500; font-size: 22.5px; line-height: 27px;
  }
  .pitch-main { top: 600px; }
  .pitch-call { top: 679px; }
  .business-card {
    position: absolute; left: 583px; top: 753px;
    width: 197px; height: 336px;
    background: radial-gradient(ellipse at 50% 40%, #2a2a2b 0%, #151516 100%);
    color: var(--card-text);
    font-family: "Open Sans", sans-serif; text-align: center;
  }
  .card-title {
    margin-top: 24px; color: var(--brand-red);
    font-style: italic; font-weight: 700; font-size: 17px;
  }
  .card-services { margin-top: 6px; font-size: 12.5px; line-height: 19px; }
  .card-owner { margin-top: 26px; font-size: 12.5px; white-space: nowrap; }
  .card-contact { margin-top: 26px; font-size: 11.5px; line-height: 19px; }
  .card-handle { margin-top: 22px; font-size: 12px; }
</style>
</head>
<body>
<div class="flyer">
  <svg class="flyer-shapes" viewBox="0 0 850 1100" width="850" height="1100">
    <defs>
      <linearGradient id="darkFade" x1="0" y1="0" x2="1" y2="1">
        <stop offset="0" stop-color="#2c2c2e"/>
        <stop offset="0.5" stop-color="#1a1a1b"/>
        <stop offset="1" stop-color="#3a3a3c"/>
      </linearGradient>
      <linearGradient id="photoTones" x1="0" y1="0" x2="1" y2="0.4">
        <stop offset="0" stop-color="#e9e4df"/>
        <stop offset="0.35" stop-color="#d9a98c"/>
        <stop offset="0.6" stop-color="#3ea0d6"/>
        <stop offset="0.85" stop-color="#c99278"/>
        <stop offset="1" stop-color="#f4f4f4"/>
      </linearGradient>
    </defs>
    <rect width="850" height="1100" fill="url(#darkFade)"/>
    <path d="M0,305 C260,150 560,40 850,0 L850,1100 L0,1100 Z" fill="#d6d6d8"/>
    <path d="M0,322 C260,168 560,56 850,12 L850,1100 L0,1100 Z" fill="var(--paper)"/>
    <path role="img" aria-label="Photo of a smiling woman in a blue sports top doing a leg stretch"
          d="M0,330 C260,176 560,64 850,20 L850,420 C620,500 300,520 0,440 Z" fill="url(#photoTones)" opacity="0.9"/>
    <rect x="514" y="428" width="336" height="600" fill="var(--panel-grey)"/>
    <path d="M0,440 C300,520 600,500 850,405 L850,412 C600,510 300,528 0,456 Z" fill="#cfcfd1"/>
    <path d="M0,463 C260,515 560,505 850,408 L850,428 C580,540 260,578 0,558 Z" fill="var(--brand-red)"/>
    <path d="M0,968 C300,1000 600,1000 850,930 L850,1100 L0,1100 Z" fill="url(#darkFade)"/>
    <path d="M0,966 C300,992 600,992 850,924 L850,930 C600,1000 300,1000 0,972 Z" fill="#cfcfd1"/>
    <path d="M240,994 C450,1012 650,1000 850,930 L850,975 C650,1015 450,1022 240,1002 Z" fill="var(--brand-red)"/>
  </svg>

  <div class="brand-name">Kessler's Fitness</div>

  <div class="trainer-photo" role="img" aria-label="Photo of the trainer sitting with crossed arms in a park under oak trees"></div>

  <h1 class="headline">Do you suffer from<br>chronic joint or back pain,<br>high blood pressure<br>or high cholesterol?</h1>

  <p class="pitch pitch-main">A personalized fitness and nutrition<br>plan can change your life.</p>
  <p class="pitch pitch-call">Let Kessler's Fitness<br>show you how.</p>

  <div class="business-card">
    <p class="card-title">Personal Training</p>
    <p class="card-services">-Online-<br>-In Your Home-<br>-Parks and Beaches-<br>-Bride, Groom, Bridal Party-</p>
    <p class="card-owner">Mark Kessler Owner/Trainer</p>
    <p class="card-contact">555-210-4836<br>kesslersfitness1@mail.com<br>www.kesslersfitness.com</p>
    <p class="card-handle">@kesslersfitness</p>
  </div>
</div>
</body>
</html>
```